Label/ sleeve for olive oil tin can

We are looking for a design of a full sleeve label for our olive oil cans. These cans contain 500ml of oil and the label should have a dimension of approximately 215mm wide and 175mm high.

Please find the first draft of the design guidelines attached as well as the brand logo.
Updates

Low design quality

Target Market(s)

Consumers

Industry/Entity Type

Olive oil

Colors
00AB8E
00BBA5
67D7C9
C6EFE9
E9F9F6

Requirements
Must have
• Full label design - around the entire bottle. Read the brief

```html
<!DOCTYPE html>
<html lang="en">
<head>
<meta charset="utf-8">
<title>Villa Solara Extra Virgin Olive Oil – Full Wrap Tin Label</title>
<link rel="stylesheet" href="https://fonts.googleapis.com/css2?family=Bellefair&family=Open+Sans:wght@400;700&family=Maven+Pro:wght@400&family=Josefin+Sans:wght@300&display=swap">
<style>
  :root {
    --page: #ffffff;
    --green-dark: #2a4d40;
    --green-mid: #3a7765;
    --gold: #c09a5a;
    --gold-strip: #bf9a5c;
    --gold-line: #c8a66c;
    --ink-light: #ffffff;
    --ink-strip: #2d4d42;
    --tree-light: #86b45c;
    --tree-dark: #3e6d34;
  }
  * { margin: 0; padding: 0; box-sizing: border-box; }
  html, body { width: 1011px; height: 1200px; overflow: hidden; background: var(--page); }
  .canvas { position: relative; width: 1011px; height: 1200px; }

  /* full wraparound label, 215 × 175 mm, laid flat */
  .wrap-label {
    position: absolute; left: 25px; top: 210px;
    width: 960px; height: 781px; display: flex;
  }

  .side-strip {
    position: relative; width: 90px; height: 100%;
    background: var(--gold-strip);
  }
  .origin-line {
    position: absolute; left: 45px; top: 330px;
    transform: translate(-50%, -50%) rotate(-90deg);
    width: 520px; text-align: center;
    font-family: "Open Sans", sans-serif; font-weight: 400;
    font-size: 17px; line-height: 1.2; letter-spacing: 1px;
    color: var(--ink-strip); text-transform: uppercase;
  }
  .volume {
    position: absolute; left: 6px; bottom: 8px;
    font-family: "Open Sans", sans-serif; font-weight: 700;
    font-size: 15px; color: var(--ink-strip);
  }

  .green-body {
    position: relative; flex: 1; height: 100%;
    background: linear-gradient(90deg,
      var(--green-dark) 0%, var(--green-mid) 25%, var(--green-dark) 50%,
      var(--green-mid) 75%, var(--green-dark) 100%);
  }

  .front-panel {
    position: absolute; left: 290px; top: 0; width: 290px; height: 100%;
    color: var(--ink-light); text-align: center;
  }

  .brand { position: absolute; left: 0; right: 0; top: 46px; }
  .brand-dot {
    width: 70px; height: 70px; border-radius: 50%;
    background: var(--gold-line); margin: 0 auto 10px;
  }
  .brand-name { font-family: "Open Sans", sans-serif; font-size: 15px; }

  .product-title { position: absolute; left: 0; right: 0; top: 178px; }
  .grade { font-family: "Bellefair", serif; font-size: 21px; letter-spacing: 2px; line-height: 1.2; }
  .product-name {
    font-family: "Bellefair", serif; font-weight: 400;
    font-size: 60px; line-height: 0.95; color: var(--gold); letter-spacing: 1px;
  }
  .product-name-el {
    font-family: "Open Sans", sans-serif; font-size: 14px; letter-spacing: 0.5px; margin-top: 4px;
  }

  .tree-art {
    position: absolute; left: 10px; top: 360px; width: 270px; height: 255px;
    border-radius: 50% 50% 22% 22% / 55% 55% 20% 20%;
    background: radial-gradient(ellipse at 50% 38%, var(--tree-light) 0%, var(--tree-dark) 75%);
  }
  .cert-mark {
    position: absolute; left: 216px; top: 522px; width: 44px; height: 44px;
    border: 2px solid var(--ink-light); border-radius: 50%;
  }

  .edition {
    position: absolute; left: 45px; right: 45px; top: 643px;
    border-top: 1px solid var(--gold-line); border-bottom: 1px solid var(--gold-line);
    padding: 7px 0 6px;
    font-family: "Maven Pro", sans-serif; font-size: 17px; letter-spacing: 1px; color: var(--gold);
  }

  .process { position: absolute; left: 60px; right: 60px; top: 702px; }
  .process-en {
    font-family: "Josefin Sans", sans-serif; font-weight: 300; font-size: 16px;
    padding-bottom: 2px; border-bottom: 1px solid var(--gold-line);
  }
  .process-el { font-family: "Open Sans", sans-serif; font-size: 11px; margin-top: 3px; letter-spacing: 0.5px; }
</style>
</head>
<body>
<div class="canvas">
  <div class="wrap-label">
    <div class="side-strip">
      <p class="origin-line">From Villa Solara's olive trees<br>on Zakynthos Island</p>
      <p class="volume">0.5 Lt.</p>
    </div>
    <div class="green-body">
      <div class="front-panel">
        <div class="brand">
          <div class="brand-dot"></div>
          <p class="brand-name">Villa Solara</p>
        </div>
        <div class="product-title">
          <p class="grade">- EXTRA VIRGIN -</p>
          <h1 class="product-name">OLIVE OIL</h1>
          <p class="product-name-el">ΕΞΤΡΑ ΠΑΡΘΕΝΟ ΕΛΑΙΟΛΑΔΟ</p>
        </div>
        <div class="tree-art" role="img" aria-label="Illustration of an old olive tree with a twisted trunk"></div>
        <div class="cert-mark" role="img" aria-label="Organic certification badge"></div>
        <p class="edition">LIMITED PRODUCTION</p>
        <div class="process">
          <p class="process-en">FIRST COLD PRESSING</p>
          <p class="process-el">ΠΡΩΤΟ ΨΥΧΡΟ ΠΙΕΣΗ</p>
        </div>
      </div>
    </div>
  </div>
</div>
</body>
</html>
```